wine label for ultra premium vineyard in Bendigo, Central Otago, New Zealand

"LARKSPUR" is our new wine brand, with grapes grown in our spectacular "ter Hoeven" vineyard. The small, elevated vineyard overlooks a river valley and snowy mountains. We would like a highly elegant label for our 2018 pinot noir wine, which highlights the quality of wine and our very special vineyard location. "LARKSPUR" has to be prominent, with secondary emphasis on "ter Hoeven vineyard" and "Bendigo, Central Otago". A stylized LARKSPUR logo (bird) could be a useful design device instead of the commonly seen illustrated mountain landscape (which is quite common for our local wines). Label size 90 high, 110 wide. Please use a pinot noir / burgundy bottle. See here for vineyard pics, and also below pics for other local wine labels and pics for inspiration / styles. https://www.instagram.com/jas.ter.hoeven.example/

Target Market(s)

average bottle price for this premium red pinot noir would be aroundUS$40. target market are generally urban professionals aged 25 and older with a high degree of interest in pinot noir wine, and who are familiar with New Zealand pinot noir (ie. already know several brands).

Colors
ed252d

Requirements
Must have
• distinctive label, sophisticated look
Nice to have
• classy white paper stock
Should not have
• label must not get too busy... less but high quality and distinctive is more....

```html
<!DOCTYPE html>
<html lang="en">
<head>
<meta charset="utf-8">
<title>Larkspur Pinot Noir – Label</title>
<link rel="stylesheet" href="https://fonts.googleapis.com/css2?family=Playfair+Display:wght@400;700&family=Questrial&display=swap">
<style>
  :root {
    --paper: #ffffff;
    --pattern-grey: #e4e4e4;
    --brand-red: #a8141b;
    --label-red: #e0202a;
    --label-red-light: #ee5860;
    --gold: #c9971f;
    --gold-light: #f0c85a;
    --ink-dark: #3a0a0c;
    --text-white: #ffffff;
  }
  * { margin: 0; padding: 0; box-sizing: border-box; }
  html, body { width: 849px; height: 1200px; overflow: hidden; background: var(--paper); }
  .board { position: relative; width: 849px; height: 1200px; background: var(--paper); }

  .pattern-field {
    position: absolute; left: 36px; top: 73px; width: 790px; height: 591px;
    background: var(--pattern-grey);
  }

  .brand-mark-dot {
    position: absolute; left: 262px; top: 212px; width: 100px; height: 100px;
    border-radius: 50%; background: var(--brand-red);
  }
  .brand-wordmark {
    position: absolute; left: 115px; top: 355px; width: 400px; text-align: center;
    font-family: "Playfair Display", serif; font-weight: 700; font-size: 96px;
    line-height: 1; color: var(--brand-red);
  }

  .label {
    position: absolute; left: 94px; top: 545px; width: 452px; height: 553px;
    background: var(--label-red); color: var(--text-white); overflow: hidden;
  }
  .label-pattern {
    position: absolute; left: 30px; right: 30px; top: 240px; bottom: 28px;
    background: linear-gradient(180deg, rgba(238,88,96,0) 0%, rgba(238,88,96,.45) 35%, rgba(238,88,96,.55) 100%);
  }
  .label-frame {
    position: absolute; left: 26px; top: 28px; width: 398px; height: 498px;
    border: 3px solid var(--gold); border-top: none;
    border-image: linear-gradient(180deg, var(--gold-light), var(--gold)) 1;
  }
  .label-dot {
    position: absolute; left: 209px; top: 50px; width: 38px; height: 38px;
    border-radius: 50%; background: var(--gold-light);
  }
  .label-name {
    position: absolute; left: 0; width: 100%; top: 150px; text-align: center;
    font-family: "Playfair Display", serif; font-weight: 700; font-size: 72px;
    line-height: 1; color: var(--text-white);
  }
  .label-rule {
    position: absolute; left: 118px; top: 238px; width: 215px; height: 1px; background: var(--ink-dark);
  }
  .label-variety {
    position: absolute; left: 0; width: 100%; top: 246px; text-align: center;
    font-family: "Questrial", sans-serif; font-size: 24px; line-height: 28px;
  }
  .label-vineyard {
    position: absolute; left: 0; width: 100%; top: 350px; text-align: center;
    font-family: "Playfair Display", serif; font-weight: 400; font-size: 40px; line-height: 44px;
  }
  .label-region {
    position: absolute; left: 0; width: 100%; top: 466px; text-align: center;
    font-family: "Playfair Display", serif; font-weight: 400; font-size: 22px; line-height: 1.2;
  }
</style>
</head>
<body>
  <main class="board">
    <div class="pattern-field" role="img" aria-label="Faint grey pattern of stylised birds in flight on distressed texture"></div>

    <div class="brand-mark-dot"></div>
    <div class="brand-wordmark">larkspur</div>

    <section class="label">
      <div class="label-pattern" role="img" aria-label="Soft pattern of stylised birds in flight, tone on tone red"></div>
      <div class="label-frame"></div>
      <div class="label-dot"></div>
      <h1 class="label-name">larkspur</h1>
      <div class="label-rule"></div>
      <p class="label-variety">premium<br>red pinot noir</p>
      <p class="label-vineyard">ter Hoeven<br>vineyard</p>
      <p class="label-region">Bendigo, Central Otago</p>
    </section>
  </main>
</body>
</html>
```